Menu Based Selling

We want a power point telling our story - www.kettlebrookprovisions.com has the info as well as our video posted on the site. I have uploaded two files specific to this - one is more narrative that can be used and the other is an excel file illustrating how a menu would look

```html
<!DOCTYPE html>
<html lang="en">
<head>
<meta charset="utf-8">
<title>Menu Based Selling – Kettlebrook Provisions</title>
<link rel="stylesheet" href="https://fonts.googleapis.com/css2?family=Poppins:wght@300;400;500;600&display=swap">
<style>
  :root{
    --canvas:#485a66;
    --slide:#ffffff;
    --ink:#1d1d1f;
    --ink-soft:#3a3a3c;
    --blue:#3b7dd0;
    --blue-deep:#3b6fc2;
    --blue-sky:#5b9bd5;
    --green:#4f9a3c;
    --green-soft:#8dc97c;
    --green-pale:#a9d08e;
    --table-head:#4472c4;
    --table-total:#70ad47;
    --table-day:#548235;
    --summary:#b4c6e7;
    --grid:#9aa3ad;
  }
  *{box-sizing:border-box;margin:0;padding:0}
  html,body{width:1200px;height:1200px;overflow:hidden}
  body{background:var(--canvas);font-family:"Poppins",sans-serif;color:var(--ink);position:relative}

  .slide{position:absolute;width:534px;height:318px;background:var(--slide);overflow:hidden}
  .slide--intro{left:44px;top:252px}
  .slide--process{left:622px;top:252px}
  .slide--steps{left:44px;top:624px}
  .slide--menu{left:622px;top:624px}

  .slide__decor{position:absolute;inset:0;width:100%;height:100%}

  .brand{position:absolute;left:19px;top:15px;display:flex;align-items:center;gap:4px;
    font-size:9px;font-weight:500;color:var(--ink-soft);letter-spacing:-.1px}
  .brand__mark{width:9px;height:9px;background:var(--green-soft)}

  /* slide 1 */
  .intro__quote{position:absolute;left:43px;top:128px;width:335px;
    font-size:17.5px;font-weight:300;line-height:1.15;color:var(--ink)}
  .intro__quote .accent-green{color:var(--green)}
  .intro__quote .accent-blue{color:var(--blue)}

  /* slide 2 */
  .process__title{position:absolute;left:43px;top:64px;width:430px;
    font-size:14px;font-weight:500;line-height:1.3}
  .process__list{position:absolute;left:46px;top:120px;width:430px;list-style:none}
  .process__list li{position:relative;padding-left:12px;margin-bottom:9px;
    font-size:8.3px;line-height:1.32;color:var(--ink-soft)}
  .process__list li::before{content:"";position:absolute;left:0;top:4px;width:3px;height:3px;border-radius:50%;background:var(--ink-soft)}

  /* slide 3 */
  .steps__title{position:absolute;left:43px;top:70px;font-size:19.5px;font-weight:400;line-height:1.2}
  .steps__title strong{display:block;color:var(--blue);font-weight:600}
  .step-card{position:absolute;background:#fff;border:1px solid #c9d4dc;border-radius:4px;
    box-shadow:0 1px 2px rgba(0,0,0,.12);display:flex;align-items:center;justify-content:center;
    text-align:center;font-size:6.6px;line-height:1.35;color:var(--ink-soft);padding:4px}
  .step-card--1{left:64px;top:172px;width:80px;height:52px}
  .step-card--2{left:171px;top:168px;width:80px;height:70px}
  .step-card--3{left:280px;top:168px;width:79px;height:56px}
  .step-card--4{left:387px;top:168px;width:80px;height:56px}

  /* slide 4 */
  .menu__heading{position:absolute;left:40px;top:31px;width:420px;text-align:center;line-height:1.2}
  .menu__kicker{font-size:7.2px;font-weight:600}
  .menu__sub{font-size:8.2px;font-weight:400}
  .menu__contact{font-size:5.8px;margin-top:6px;color:var(--ink-soft)}
  .menu-table{position:absolute;left:46px;top:90px;width:420px;border-collapse:collapse;table-layout:fixed;
    font-size:4.3px;line-height:1}
  .menu-table th,.menu-table td{border:0.5px solid var(--grid);height:8.6px;padding:0 2px;white-space:nowrap;overflow:hidden;background:#fff}
  .menu-table thead th{background:var(--table-head);color:#fff;font-weight:500;text-align:center}
  .menu-table .meal{font-weight:500;border-bottom-color:#fff}
  .menu-table .cost{text-align:right}
  .menu-table .row-total td{background:var(--table-total);color:#fff;font-weight:600}
  .menu-table .row-total td.label{background:#fff;color:var(--ink)}
  .menu-table .row-day td{background:var(--table-day);color:#fff;font-weight:600}
  .menu-summary{position:absolute;left:46px;top:254px;width:76px;border-collapse:collapse;font-size:4.3px}
  .menu-summary td{background:var(--summary);border:0.5px solid var(--grid);height:10px;padding:0 2px;font-weight:500}
  .menu-summary td:last-child{text-align:right}
</style>
</head>
<body>

<!-- Slide 1 : headline -->
<section class="slide slide--intro">
  <svg class="slide__decor" viewBox="0 0 467 278" preserveAspectRatio="none" aria-hidden="true">
    <defs>
      <linearGradient id="meal-tones" x1="0" y1="0" x2="1" y2="1">
        <stop offset="0" stop-color="#e4ebe6"/>
        <stop offset=".45" stop-color="#9fb77a"/>
        <stop offset=".8" stop-color="#d98a45"/>
        <stop offset="1" stop-color="#7f9fa3"/>
      </linearGradient>
    </defs>
    <polygon points="400,0 428,0 382,118 354,118" fill="var(--blue)"/>
    <polygon points="418,0 467,0 467,205 345,205" fill="url(#meal-tones)" role="img" aria-label="Plated meal of roasted vegetables, grains and fresh herbs"/>
    <polygon points="467,150 467,278 426,278" fill="var(--green-soft)"/>
  </svg>
  <div class="brand"><span class="brand__mark"></span>Kettlebrook Provisions</div>
  <p class="intro__quote">It is not the price of <span class="accent-green">“Green Beans”</span> that you should be concerned about&nbsp; - it is the price for <span class="accent-blue">the meal.</span></p>
</section>

<!-- Slide 2 : menu creation process -->
<section class="slide slide--process">
  <svg class="slide__decor" viewBox="0 0 467 278" preserveAspectRatio="none" aria-hidden="true">
    <polygon points="446,0 467,0 467,22 442,86 420,86" fill="var(--blue)"/>
    <polygon points="467,150 467,278 410,278" fill="var(--green-soft)"/>
  </svg>
  <div class="brand"><span class="brand__mark"></span>Kettlebrook Provisions</div>
  <h2 class="process__title">With Kettlebrook Provisions' dynamic menu creation process we can help create meals that meet your budget.</h2>
  <ul class="process__list">
    <li>You can use our standard priced menus and pick and chose by day of week – meal selection&nbsp; to meet your budget.&nbsp; If you are trying to hit a target price on a weekly basis&nbsp; - the daily costs can vary as long as the week balances.</li>
    <li>Are you working within the CACFP or NSPL reimbursement guidelines and wanting to offer creative, fun and tasty food to the children you serve&nbsp; - we can help.</li>
    <li>Whether you have a ready-to-serve requirement of made-from-scratch kitchen we can work with you to design a menu that meets not only the nutritional requirements but the monetary ones as well.</li>
  </ul>
</section>

<!-- Slide 3 : four steps -->
<section class="slide slide--steps">
  <svg class="slide__decor" viewBox="0 0 467 278" preserveAspectRatio="none" aria-hidden="true">
    <polygon points="450,15 476,15 412,205 386,205" fill="var(--blue)"/>
    <polygon points="467,125 467,278 418,278" fill="var(--green-soft)"/>
    <polygon points="57,134 135,134 145,148.5 135,163 57,163 67,148.5" fill="var(--blue-deep)"/>
    <polygon points="130,134 212,134 222,148.5 212,163 130,163 140,148.5" fill="var(--blue-sky)"/>
    <polygon points="222,134 306,134 316,148.5 306,163 222,163 232,148.5" fill="var(--green)"/>
    <polygon points="316,134 400,134 410,148.5 400,163 316,163 326,148.5" fill="var(--green-soft)"/>
  </svg>
  <div class="brand"><span class="brand__mark"></span>Kettlebrook Provisions</div>
  <h2 class="steps__title">How we create a plan for you in <strong>4 simple steps</strong></h2>
  <div class="step-card step-card--1">we identify your weekly budget</div>
  <div class="step-card step-card--2">what meals you are serving (breakfast, lunch, snack(s) and/or dinner)</div>
  <div class="step-card step-card--3">We discuss your capabilities as it relates to preparation</div>
  <div class="step-card step-card--4">We’re ready to make your personalized plan</div>
</section>

<!-- Slide 4 : sample priced menu -->
<section class="slide slide--menu">
  <svg class="slide__decor" viewBox="0 0 467 278" preserveAspectRatio="none" aria-hidden="true">
    <polygon points="446,18 472,18 430,200 404,200" fill="var(--blue)"/>
    <polygon points="467,140 467,278 424,278" fill="var(--green-soft)"/>
  </svg>
  <div class="brand"><span class="brand__mark"></span>Kettlebrook Provisions</div>
  <div class="menu__heading">
    <p class="menu__kicker">SAMPLE!&nbsp; WEEK VIEW RESIDENTIAL PROGRAM</p>
    <p class="menu__sub">March 2022 Breakfast, Snack, Lunch and Dinner priced Menu prepared exclusively for</p>
    <p class="menu__sub">“Your Organization”</p>
    <p class="menu__contact">for questions please contact your sales rep info@kettlebrookprovisions.com - 555.201.7734</p>
  </div>

  <table class="menu-table">
    <colgroup>
      <col style="width:40px">
      <col style="width:55px"><col style="width:21px">
      <col style="width:55px"><col style="width:21px">
      <col style="width:55px"><col style="width:21px">
      <col style="width:55px"><col style="width:21px">
      <col style="width:55px"><col style="width:21px">
    </colgroup>
    <thead>
      <tr><th>Week 1</th><th colspan="2">Monday</th><th colspan="2">Tuesday</th><th colspan="2">Wednesday</th><th colspan="2">Thursday</th><th colspan="2">Friday</th></tr>
    </thead>
    <tbody>
      <tr><td class="meal">Breakfast</td><td>Milk</td><td class="cost">$0.21</td><td>Milk</td><td class="cost">$0.21</td><td>Milk</td><td class="cost">$0.21</td><td>Milk</td><td class="cost">$0.21</td><td>Milk</td><td class="cost">$0.21</td></tr>
      <tr><td></td><td>Bagel</td><td class="cost">$0.22</td><td>Oatmeal</td><td class="cost">$0.19</td><td>Pancakes</td><td class="cost">$0.31</td><td>Cheese Grits</td><td class="cost">$0.18</td><td>Scrambled Eggs</td><td class="cost">$0.25</td></tr>
      <tr><td></td><td>Fresh Fruit</td><td class="cost">$0.27</td><td>Strawberries</td><td class="cost">$0.30</td><td>Applesauce</td><td class="cost">$0.15</td><td>Banana</td><td class="cost">$0.17</td><td>Orange Slices</td><td class="cost">$0.20</td></tr>
      <tr class="row-total"><td class="label">Total Breakfast</td><td></td><td class="cost">$0.70</td><td></td><td class="cost">$0.70</td><td></td><td class="cost">$0.67</td><td></td><td class="cost">$0.56</td><td></td><td class="cost">$0.66</td></tr>
      <tr><td class="meal">Snack</td><td>Yogurt</td><td class="cost">$0.24</td><td>Graham Crackers</td><td class="cost">$0.14</td><td>Pretzels</td><td class="cost">$0.12</td><td>String Cheese</td><td class="cost">$0.25</td><td>Trail Mix</td><td class="cost">$0.28</td></tr>
      <tr><td></td><td>Juice</td><td class="cost">$0.18</td><td>Milk</td><td class="cost">$0.21</td><td>Apple</td><td class="cost">$0.19</td><td>Grapes</td><td class="cost">$0.22</td><td>Juice</td><td class="cost">$0.18</td></tr>
      <tr class="row-total"><td class="label">Total Snack</td><td></td><td class="cost">$0.42</td><td></td><td class="cost">$0.35</td><td></td><td class="cost">$0.31</td><td></td><td class="cost">$0.47</td><td></td><td class="cost">$0.46</td></tr>
      <tr><td class="meal">Lunch</td><td>Turkey Wrap</td><td class="cost">$0.62</td><td>Chicken Strips</td><td class="cost">$0.58</td><td>Pizza Slice</td><td class="cost">$0.49</td><td>Beef Tacos</td><td class="cost">$0.66</td><td>Baked Fish</td><td class="cost">$0.71</td></tr>
      <tr><td></td><td>Side Salad</td><td class="cost">$0.21</td><td>Green Beans</td><td class="cost">$0.12</td><td>Corn</td><td class="cost">$0.11</td><td>Rice</td><td class="cost">$0.09</td><td>Peas and Carrots</td><td class="cost">$0.14</td></tr>
      <tr><td></td><td>Milk</td><td class="cost">$0.21</td><td>Milk</td><td class="cost">$0.21</td><td>Milk</td><td class="cost">$0.21</td><td>Milk</td><td class="cost">$0.21</td><td>Milk</td><td class="cost">$0.21</td></tr>
      <tr class="row-total"><td class="label">Total Lunch</td><td></td><td class="cost">$1.04</td><td></td><td class="cost">$0.91</td><td></td><td class="cost">$0.81</td><td></td><td class="cost">$0.96</td><td></td><td class="cost">$1.06</td></tr>
      <tr><td class="meal">Dinner</td><td>Meatloaf</td><td class="cost">$0.74</td><td>Baked Chicken</td><td class="cost">$0.69</td><td>Pasta Bake</td><td class="cost">$0.52</td><td>Pork Chop</td><td class="cost">$0.78</td><td>Chili</td><td class="cost">$0.55</td></tr>
      <tr><td></td><td>Mashed Potatoes</td><td class="cost">$0.16</td><td>Broccoli</td><td class="cost">$0.18</td><td>Garden Salad</td><td class="cost">$0.22</td><td>Sweet Potato</td><td class="cost">$0.17</td><td>Cornbread</td><td class="cost">$0.13</td></tr>
      <tr><td></td><td>Dinner Roll</td><td class="cost">$0.09</td><td>Dinner Roll</td><td class="cost">$0.09</td><td>Garlic Bread</td><td class="cost">$0.11</td><td>Dinner Roll</td><td class="cost">$0.09</td><td>Milk</td><td class="cost">$0.21</td></tr>
      <tr class="row-total"><td class="label">Total Dinner</td><td></td><td class="cost">$0.99</td><td></td><td class="cost">$0.96</td><td></td><td class="cost">$0.85</td><td></td><td class="cost">$1.04</td><td></td><td class="cost">$0.89</td></tr>
      <tr class="row-day"><td>Total Day</td><td></td><td class="cost">$3.15</td><td></td><td class="cost">$2.92</td><td></td><td class="cost">$2.64</td><td></td><td class="cost">$3.03</td><td></td><td class="cost">$3.07</td></tr>
    </tbody>
  </table>

  <table class="menu-summary">
    <tr><td>Weekly Total</td><td>$14.81</td></tr>
    <tr><td>Daily Average</td><td>$2.96</td></tr>
    <tr><td>Daily Budget</td><td>$3.50</td></tr>
    <tr><td>Savings vs Budget</td><td>$0.54</td></tr>
    <tr><td>% Savings</td><td>15%</td></tr>
  </table>
</section>

</body>
</html>
```